Ecommerce Web Design (E - File Copyright Denver, CO)

This is a service style web design. It is a stand alone website that will eventually be linked to another website (quenvoril.com). But for the time being it is a stand alone website. It will only offer 3-4 products (Services) but have a gallery page with tabs for selling copyrighted material for clients like Tumbrel. I will require the following pages:

Only Web Pages, No Coding

Home Page
Products Page
Customer Registration Page
Copyright Information Page (Is being done by a third party for now)
Store for Gallery of all Copyrighted material (with Tabs for Photo, Art, Literature, Manuscripts, Video, etc) to quenvoril.com
Blog Page
About Us Page/Contact US page (all on same page)
User agreement & Privacy Statement Page
Page to look at the borrowers Copyright Files (will be linked to a DB for access via customer unique password and login
FAQ Page

My customers will be Authors, Artist, Photographers, Playwright's, Lawyers, Film rights, software and Corporate Web Designers. We are a third party electronic copyright service offering protection of intellectual property. The site needs to convey Trust, Integrity, Stability, Safety and Strength. I also want to appeal to the artist creativity and want the site to look friendly, hence the logo design. Simple colorful. The site will also have links to social media, Chatterbox, Vexmo+, WorkNest and Chirpzy.

Competitor Website:
plavetu.com
http://zandorislab.com/
http://trelkovine.example.com/2011/03/tumbrel-alternative-image-hosting-and.html

The ecommerce will offer payment from Coinmarsh, Orvex, TallyCard and Brivo via quillpayhub. The site will also have SSL certificate.

Product 1- Online Copyright Registration
Product 2- Update to Copyright Registration
Product 3- File Copyright to Federal Works Registry (National Archive Hall)

The company logo is attached to this file for your preview. I will require additional logos or Icons for all three products (The copy of the National Archive Hall is also attached for your preview) please feel free to use your own version for the logos/Icons. I'm not a designer and lack artistic impressions as to what I want, but when I see the designs I will know if its the right one.

The website will function as a registration point for Intellectual property copyrights and will also function as a source for infringement searches of the material online. The term "Third Party Electronic Copyright Protection" should be used on the Home Page. Please if you have any questions please ask. I will respond to all entries and correspondence. I work from home and have the ability to respond at a moments notice. That being said I am located in Denver, CO USA, so keep in mind my time zone when you send correspondence to me.

Good morning or Evening all, There are 10 days left to get your design ideas in. I am very pleased with the results so far. Make sure to email me if you have any questions. Have a great day everyone. Gerald

```html
<!DOCTYPE html>
<html lang="en">
<head>
<meta charset="utf-8">
<title>Vaultmark Copyright – Home</title>
<link href="https://fonts.googleapis.com/css2?family=Open+Sans:wght@400;600;700&family=Ubuntu:wght@300;400;500&display=swap" rel="stylesheet">
<style>
:root{
  --green:#7dc242;
  --green-bright:#8ccf3f;
  --header:#2a2a2a;
  --strip:#2d2d2d;
  --strip-dark:#121212;
  --panel:#1e1e1e;
  --footer:#2b2b2b;
  --footer-bottom:#0f0f0f;
  --white:#ffffff;
  --text:#2e2e2e;
  --muted:#9a9a9a;
  --rule:#dcdcdc;
}
*{margin:0;padding:0;box-sizing:border-box}
html,body{width:781px;height:1200px;overflow:hidden;background:#fff}
body{position:relative;font-family:'Ubuntu',sans-serif;color:var(--text)}
.abs{position:absolute}

/* header */
.site-header{left:0;top:0;width:781px;height:44px;background:var(--header)}
.brand{left:72px;top:12px;display:flex;align-items:center;gap:7px;color:var(--white);font-family:'Ubuntu',sans-serif;font-weight:400;font-size:17px;line-height:20px}
.brand-mark{width:16px;height:16px;background:var(--green)}
.main-nav{left:245px;top:0;height:44px;display:flex}
.main-nav a{display:block;height:44px;line-height:48px;padding:0 9px;font-size:8px;color:#c4c4c4;text-decoration:none}
.main-nav a.active{background:var(--green);color:#fff;padding:0 8px}

/* hero */
.hero{left:0;top:44px;width:781px;height:398px;
  background:linear-gradient(100deg,#3a3a38 0%,#4d4c48 30%,#6aa0b0 48%,#3bb3c8 62%,#7ec6d9 80%,#9ad0e4 100%)}
.hero-shade{left:0;top:344px;width:781px;height:98px;background:linear-gradient(180deg,rgba(40,40,38,0) 0%,rgba(40,40,38,.85) 100%)}
.hero-caption{left:70px;top:201px;width:289px;height:117px;background:rgba(25,25,25,.75);padding:7px 8px 0 12px;color:#fff}
.hero-caption h1{font-weight:400;font-size:18px;line-height:26px;letter-spacing:-.3px;white-space:nowrap}
.hero-caption p{margin-top:5px;font-weight:300;font-size:10.3px;line-height:16px}

/* services */
.services{left:0;top:442px;width:781px;height:77px;background:var(--strip)}
.service{top:442px;height:77px;border-top:3px solid var(--green);color:#fff}
.service.featured{background:var(--strip-dark)}
.service h3{position:absolute;top:11px;font-size:10.5px;font-weight:500;white-space:nowrap}
.service.featured h3{color:var(--green)}
.service p{position:absolute;left:7px;top:35px;right:6px;font-size:8px;line-height:12px;font-weight:300}
.service-icon{top:418px;width:52px;height:52px}

/* gallery */
.section-title{left:72px;top:552px;width:638px;height:36px;display:flex;align-items:center;gap:8px}
.section-title .rule{flex:1;height:4px;border-top:1px solid var(--rule);border-bottom:1px solid var(--rule)}
.section-title h2{font-family:'Open Sans',sans-serif;font-weight:400;font-size:24px;color:#333}
.section-title h2 span{color:var(--green);font-weight:700}
.filters{left:0;top:597px;width:781px;text-align:center;font-size:9.5px;color:#333}
.filters .on{color:var(--green)}

.gallery-intro{left:72px;top:632px;width:274px;height:200px;background:var(--panel)}
.intro-box{left:109px;top:671px;width:200px;height:122px;border:1px solid #777;padding:6px 9px}
.intro-box h4{font-family:'Open Sans',sans-serif;font-weight:400;font-size:18px;color:#fff;line-height:24px;white-space:nowrap}
.intro-box h4 span{color:var(--green);font-weight:700}
.intro-box p{margin-top:2px;font-family:'Open Sans',sans-serif;font-size:8px;line-height:14.3px;color:var(--muted)}
.photo{display:block}
.tagline{left:346px;top:830px;width:364px;height:44px;background:var(--green-bright);color:#fff;font-family:'Open Sans',sans-serif;font-weight:700;font-size:14.5px;line-height:44px;text-align:center}
.video-bar{left:346px;top:988px;width:182px;height:28px;background:rgba(20,20,20,.7)}
.video-bar .label{position:absolute;left:14px;top:7px;font-size:11px;color:#fff}
.video-bar .more{position:absolute;right:10px;top:10px;font-size:7.5px;color:var(--green);font-style:italic}

/* footer */
.site-footer{left:0;top:1066px;width:781px;height:96px;background:var(--footer)}
.divider{top:1066px;width:1px;height:96px;background:#4a4a4a}
.contact{top:1106px;display:flex;align-items:center;gap:9px;color:#fff;font-family:'Open Sans',sans-serif;font-weight:600;font-size:11.5px}
.socials{left:526px;top:1103px;width:250px;display:flex;gap:3px}
.socials span{display:flex;align-items:center;justify-content:center;height:20px;padding:0 4px;border:1.5px solid #ccc;border-radius:10px;font-size:7px;color:#ddd;white-space:nowrap}
.socials span.first{border-color:var(--green);color:var(--green)}
.copyright{left:0;top:1162px;width:781px;height:38px;background:var(--footer-bottom);color:#ddd;font-size:8px;line-height:38px;text-align:center}
</style>
</head>
<body>

<header class="abs site-header"></header>
<div class="abs brand"><span class="brand-mark"></span>Vaultmark</div>
<nav class="abs main-nav">
  <a class="active" href="#">Home</a>
  <a href="#">Products</a>
  <a href="#">Customer Registration</a>
  <a href="#">Copyright Information</a>
  <a href="#">Blog</a>
  <a href="#">About Us</a>
  <a href="#">User agreement</a>
  <a href="#">FAQ</a>
</nav>

<div class="abs hero" role="img" aria-label="Photo of a rocky sea cliff arching over a beach with turquoise water and a cloudy blue sky"></div>
<div class="abs hero-shade"></div>
<div class="abs hero-caption">
  <h1>Protect your Copyrights, Online<br>and for Free!</h1>
  <p>Lorem ipsum dolor sit amet, consectetur adipisicing elit, sed do eiusmod tempor incididunt ut labore et dolore magna aliqua.</p>
</div>

<div class="abs services"></div>
<section class="abs service featured" style="left:72px;width:210px">
  <h3 style="left:47px">Online Copyright Registration</h3>
  <p>Lorem ipsum dolor sit amet, consectetur adipisicing elit, sed do eiusmod tempor incididunt ut labore et dolore magna aliqua.</p>
</section>
<section class="abs service" style="left:290px;width:212px">
  <h3 style="left:50px">Update to Copyright Registration</h3>
  <p>Lorem ipsum dolor sit amet, consectetur adipisicing elit, sed do eiusmod tempor incididunt ut labore et dolore magna aliqua.</p>
</section>
<section class="abs service" style="left:508px;width:202px">
  <h3 style="left:50px">File Copyright to US...</h3>
  <p>Lorem ipsum dolor sit amet, consectetur adipisicing elit, sed do eiusmod tempor incididunt ut labore et dolore magna aliqua.</p>
</section>

<svg class="abs service-icon" style="left:70px" viewBox="0 0 52 52"><rect x="11" y="11" width="30" height="30" transform="rotate(45 26 26)" fill="#7dc242"/><rect x="17" y="18" width="18" height="13" fill="none" stroke="#fff" stroke-width="1.6"/><path d="M21 35h10M26 31v4" stroke="#fff" stroke-width="1.6"/></svg>
<svg class="abs service-icon" style="left:289px" viewBox="0 0 52 52"><rect x="11" y="11" width="30" height="30" transform="rotate(45 26 26)" fill="#7dc242"/><path d="M19 15h10l5 5v16H19z" fill="none" stroke="#fff" stroke-width="1.6"/><path d="M22 22h8M22 26h8M22 30h5" stroke="#fff" stroke-width="1.4"/><circle cx="31" cy="33" r="4" fill="#7dc242" stroke="#fff" stroke-width="1.4"/></svg>
<svg class="abs service-icon" style="left:507px" viewBox="0 0 52 52"><rect x="11" y="11" width="30" height="30" transform="rotate(45 26 26)" fill="#7dc242"/><rect x="17" y="22" width="18" height="12" fill="#fff"/><path d="M18 22l3-5h10l3 5" fill="none" stroke="#fff" stroke-width="1.6"/><path d="M23 26h6" stroke="#7dc242" stroke-width="1.6"/></svg>

<div class="abs section-title"><span class="rule"></span><h2>Our <span>Gallery</span></h2><span class="rule"></span></div>
<div class="abs filters"><span class="on">All</span> / Business / Inspiration / Lifestyle / Nature / Technology</div>

<div class="abs gallery-intro"></div>
<div class="abs intro-box">
  <h4>Vaultmark <span>Gallery</span></h4>
  <p>Lorem ipsum dolor sit consectetur adipisicing elit sed do eiusmod tempor incididunt labore dolore magna aliqua ut enim ad minimveniam quis nostrud exercitation uamco laboris nisi ut aliquip ex ea commodo consequat duis aute irure dolor in reprehenderit.</p>
</div>
<div class="abs photo" style="left:72px;top:832px;width:274px;height:184px;background:linear-gradient(160deg,#55524d,#3e3b37 60%,#2d2b29)" role="img" aria-label="Photo of a mountain biker riding over a large rock"></div>
<div class="abs photo" style="left:346px;top:632px;width:364px;height:198px;background:linear-gradient(180deg,#0d1a2c 0%,#24476f 45%,#6d93b9 85%,#9fb6c8 100%)" role="img" aria-label="Photo of a long suspension bridge under a deep blue sky"></div>
<div class="abs tagline">United States largest Online Copyright Service</div>
<div class="abs photo" style="left:346px;top:874px;width:182px;height:142px;background:linear-gradient(180deg,#c9ccc7,#a8aca6 60%,#7b7a72)" role="img" aria-label="Painting of a tall tree with a reddish trunk in a pale landscape"></div>
<svg class="abs" style="left:414px;top:922px" width="46" height="46" viewBox="0 0 46 46"><circle cx="23" cy="23" r="21" fill="rgba(0,0,0,.55)" stroke="#fff" stroke-width="2.5"/><path d="M18 14l13 9-13 9z" fill="#fff"/></svg>
<div class="abs video-bar"><span class="label">Videos</span><span class="more">More...</span></div>
<div class="abs photo" style="left:528px;top:874px;width:182px;height:142px;background:radial-gradient(circle at 60% 50%,#6f6257,#4b4640 70%)" role="img" aria-label="Photo of a kitten playing with a red ribbon"></div>

<footer class="abs site-footer"></footer>
<div class="abs divider" style="left:318px"></div>
<div class="abs divider" style="left:510px"></div>
<div class="abs contact" style="left:98px">
  <svg width="26" height="16" viewBox="0 0 26 16"><rect width="26" height="16" fill="#7dc242"/><path d="M1 1l12 8 12-8M1 15l9-7M25 15l-9-7" fill="none" stroke="#2b2b2b" stroke-width="1.5"/></svg>
  admin@vaultmark.net
</div>
<div class="abs contact" style="left:354px">
  <svg width="18" height="20" viewBox="0 0 18 20"><path d="M4 1l4 5-2 3c1 2 3 4 5 5l3-2 4 4-3 3C9 19 1 11 0 5z" fill="#7dc242"/></svg>
  +12 (0)555 214 807
</div>
<div class="abs socials">
  <span class="first">Chatterbox</span><span>Vexmo+</span><span>Chirpzy</span><span>Mail</span><span>Snapfolio</span>
</div>
<div class="abs copyright">Copyright © 2014 Vaultmark .All rights reserved</div>

</body>
</html>
```